Homes, Invest in Non-performing loans

We need only 3 web pages, one for the home, one for the content, one for the properties.
The main focus of our business is to offer non performing loans (before foreclosures) to the general public. All the non-performing mortgages will end in a house, an apartment, a store, etc.
Our customers are able to invest from 10,000usd to 1,000,000usd (average 50,000usd).
Our customers' usual focus groups are employees who want second earnings, perceiving the business feeling without outlay time. They look for a solid finance sense corporation that confers them certainty.
Nearly all our clients desire the house, apartment, store, etc. more than the actual earnings.
The name of our company is BRAMLEX
Reason: We value the time and effort you already invest in our project. We realize that we did't come back on some of the doubts requested by the designers. It will be inequitable to the designers who prerequisite our feedback. We also appreciate the comprehension of the community in this postponement.
Reason: Designers,
We really apreciate all the time and effort you put on our project. From the begining we ask for 3 pages, so now we will leave the 10 finalist and provide some extra time to submit the other 2 pages.
We will race the price in 10%
Target Market(s)
Our customers average investors works as employees and want to have a second income or business without spending time. (People from 35 to 50)
Industry/Entity Type
Finance
Requirements
Should not have
- FLASH

```html
<!DOCTYPE html>
<html lang="en">
<head>
<meta charset="utf-8">
<title>BRAMLEX – Remates Hipotecarios</title>
<link rel="stylesheet" href="https://fonts.googleapis.com/css2?family=Arimo:ital,wght@0,400;0,700;1,400&display=swap">
<style>
:root{
  --bar:#3c3c3c;
  --white:#ffffff;
  --olive:#a9a43b;
  --olive-light:#bdb84c;
  --olive-dark:#8f8a2a;
  --olive-text:#7d7a1f;
  --accent:#d8d23a;
  --text:#666666;
  --muted:#999999;
  --ink:#2f2f2f;
  --line:#dcdcdc;
}
*{margin:0;padding:0;box-sizing:border-box}
html,body{width:1104px;height:1200px;overflow:hidden}
body{font-family:"Arimo",Arial,sans-serif;background:linear-gradient(#e6e6e6,#f1f1f1);color:var(--text);position:relative}
.abs{position:absolute}
.topbar{left:0;top:0;width:1104px;height:50px;background:var(--bar);border-bottom:2px solid #2c2c2c;color:#fff;font-size:16px;line-height:50px;text-align:right;padding-right:84px}
.topbar .hl{color:var(--accent)}
.topbar .sep{margin:0 22px}
.sheet{left:86px;top:113px;width:932px;height:1002px;background:var(--white)}
.logo{left:92px;top:96px;width:152px}
.logo .mark{display:flex;align-items:center;gap:7px;height:44px}
.logo .sq{width:20px;height:20px;background:var(--olive);flex:none}
.logo .name{font-size:30px;font-weight:700;color:var(--ink);line-height:44px;letter-spacing:-0.5px}
.logo .tag{margin-top:22px;font-size:9px;letter-spacing:1.9px;color:#333;white-space:nowrap}
.search{left:816px;top:66px;width:202px;height:29px;border-radius:3px;background:linear-gradient(#bfbfbf,#a9a9a9);font-style:italic;font-size:13px;color:#333;line-height:29px;padding-left:16px}
.search .btn{position:absolute;right:6px;top:5px;width:20px;height:19px;background:#555;border-radius:2px}
.nav{left:250px;top:121px;width:763px;height:52px;display:flex;background:linear-gradient(var(--olive-light),var(--olive));border:1px solid var(--olive-dark)}
.nav a{color:#fff;text-decoration:none;font-size:14px;display:flex;align-items:center;justify-content:center;border-right:1px solid var(--olive-dark)}
.nav a:last-child{border-right:0}
.nav a.active{background:linear-gradient(var(--olive),var(--olive-dark))}
.slider{left:92px;top:183px;width:921px;height:280px;background:linear-gradient(90deg,#e3e3e3,#f3f3f3 60%,#e4e4e4)}
.slider .photo{position:absolute;left:0;top:0;width:520px;height:280px;background:radial-gradient(ellipse at 35% 55%,#cfd5dc,#e2e2e2 70%)}
.slider .copy{position:absolute;left:506px;top:60px;width:386px;font-size:20px;line-height:28px;color:#333;text-align:justify}
.slider .more{position:absolute;left:506px;top:125px;width:86px;height:33px;border-radius:3px;background:linear-gradient(#8a8a8a,#606060);color:#fff;font-size:14px;line-height:33px;text-align:center}
.dots{position:absolute;left:793px;top:240px;display:flex;gap:14px}
.dots i{width:16px;height:16px;border-radius:50%;background:#bfbfbf;border:2px solid #fff;display:block}
.dots i.on{background:var(--olive)}
.welcome{left:96px;top:489px;width:658px}
.welcome h1{font-size:21px;font-weight:400;color:var(--olive-text);margin-bottom:13px}
.welcome p{font-size:12.5px;line-height:21px;text-align:justify}
.welcome-photo{left:771px;top:497px;width:236px;height:146px;border:3px solid #ccc;border-radius:3px;background:linear-gradient(90deg,#d7dce0,#a59a84 60%,#5b5a52)}
.rule{left:92px;top:673px;width:916px;height:1px;background:var(--line)}
.col{top:688px;width:295px;height:412px;background:linear-gradient(#fafafa,#fff)}
.col h2{height:40px;background:linear-gradient(#6a6a6a,#4a4a4a);color:#fff;font-size:18px;font-weight:400;line-height:40px;padding-left:45px;position:relative}
.col h2 .ico{position:absolute;left:12px;top:11px;width:22px;height:18px;border-radius:3px}
.col ul{list-style:none;padding:22px 20px 0 27px}
.col li{position:relative;padding-left:19px;font-size:13px;line-height:20px;color:#666;height:78px}
.col li:nth-child(4){margin-top:9px}
.col li::before{content:"";position:absolute;left:0;top:5px;border-left:6px solid #555;border-top:4px solid transparent;border-bottom:4px solid transparent}
.col li em{display:block;font-size:10.5px;color:var(--muted);margin-top:2px}
.col .all{position:absolute;right:-3px;bottom:0;width:101px;height:27px;background:#eee;font-size:12px;color:#999;text-align:center;line-height:27px}
.footer-links{left:92px;top:1135px;font-size:12px;color:#777}
.footer-links span{margin:0 8px;color:#999}
.copyright{left:92px;top:1165px;font-size:12px;color:#777}
.social{left:957px;top:1146px;display:flex;gap:8px}
.social i{width:22px;height:22px;background:#8f99a8;display:block;border-radius:2px}
</style>
</head>
<body>
<div class="abs topbar">Call us : <span class="hl">555 014 2290</span><span class="sep">|</span>E-mail : <span class="hl">info@bramlex.com</span></div>

<div class="abs sheet"></div>

<div class="abs logo">
  <div class="mark"><span class="sq"></span><span class="name">BRAMLEX</span></div>
  <div class="tag">REMATES HIPOTECARIOS</div>
</div>

<div class="abs search">Search<span class="btn"></span></div>

<nav class="abs nav">
  <a class="active" style="width:93px">Home</a>
  <a style="width:110px">About Us</a>
  <a style="width:130px">Our Services</a>
  <a style="width:96px">Loans</a>
  <a style="width:129px">Testimonials</a>
  <a style="width:120px">Contact Us</a>
  <a style="width:85px">FAQ</a>
</nav>

<section class="abs slider">
  <div class="photo" role="img" aria-label="Young couple sitting on the floor of a bright new home"></div>
  <p class="copy">Our customers will invest from 10,000usd to 1,000,000usd (average 50,000usd).</p>
  <div class="more">View more</div>
  <div class="dots"><i class="on"></i><i></i><i></i><i></i></div>
</section>

<section class="abs welcome">
  <h1>Welcome to our site</h1>
  <p>Sed ut perspiciatis unde omnis iste natus error sit voluptatem accusantium doloremque laudantium, totam rem aperiam, eaque ipsa quae ab illo inventore veritatis et quasi architecto beatae vitae dicta sunt explicabo. Nemo enim ipsam voluptatem quia voluptas sit aspernatur aut odit aut fugit, sed quia consequuntur magni dolores eos qui ratione voluptatem sequi nesciunt. Neque porro quisquam est, qui dolorem ipsum quia dolor sit amet, consectetur, adipisci velit, sed quia non numquam eius modi tempora incidunt ut labore et dolore magnam aliquam quaerat voluptatem. Ut enim ad minima veniam, ., nisi ut aliquid ex ea commodi consequatur.</p>
</section>
<div class="abs welcome-photo" role="img" aria-label="Couple receiving the keys to their new home"></div>

<div class="abs rule"></div>

<section class="abs col" style="left:91px">
  <h2><span class="ico" style="background:#a0522d"></span>Our Services</h2>
  <ul>
    <li>Neque porro quisquam est, qui dolorem ipsum quia dolor sit amet.<em>View more</em></li>
    <li>Neque porro quisquam est, qui dolorem ipsum quia dolor sit amet.<em>View more</em></li>
    <li>Neque porro quisquam est, qui dolorem ipsum quia dolor sit amet.<em>View more</em></li>
    <li>Neque porro quisquam est, qui dolorem ipsum quia dolor sit amet.<em>View more</em></li>
  </ul>
  <div class="all">VIEW ALL</div>
</section>

<section class="abs col" style="left:399px">
  <h2><span class="ico" style="background:#cfcfcf"></span>Latest News</h2>
  <ul>
    <li>Neque porro quisquam est, qui dolorem ipsum quia dolor sit amet.<em>December 13, 2012</em></li>
    <li>Neque porro quisquam est, qui dolorem ipsum quia dolor sit amet.<em>December 13, 2012</em></li>
    <li>Neque porro quisquam est, qui dolorem ipsum quia dolor sit amet.<em>December 13, 2012</em></li>
    <li>Neque porro quisquam est, qui dolorem ipsum quia dolor sit amet.<em>December 13, 2012</em></li>
  </ul>
  <div class="all">VIEW MORE</div>
</section>

<section class="abs col" style="left:707px">
  <h2><span class="ico" style="background:#e6e6e6;border-radius:50%"></span>Testimonials</h2>
  <ul>
    <li>Neque porro quisquam est, qui dolorem ipsum quia dolor sit amet.<em>Client Name, City</em></li>
    <li>Neque porro quisquam est, qui dolorem ipsum quia dolor sit amet.<em>Client Name, City</em></li>
    <li>Neque porro quisquam est, qui dolorem ipsum quia dolor sit amet.<em>Client Name, City</em></li>
    <li>Neque porro quisquam est, qui dolorem ipsum quia dolor sit amet.<em>Client Name, City</em></li>
  </ul>
  <div class="all">VIEW MORE</div>
</section>

<footer>
  <div class="abs footer-links">Home<span>|</span>About Us<span>|</span>Our Services<span>|</span>Loans<span>|</span>Testimonials<span>|</span>Contact Us<span>|</span>FAQ</div>
  <div class="abs copyright">Copyright ©&nbsp; 2012 &nbsp;&nbsp; www.bramlex.com &nbsp;&nbsp; All rights reserved.</div>
  <div class="abs social" aria-label="Social links"><i></i><i></i></div>
</footer>
</body>
</html>
```